Flyer Design

Create a flyer using the logo theme. Single page for to be sent out on email. Attached is an image of the layout, below is the text. A5 and a4 versions.

Simplifying the MAZE

This short workshop is designed as a refresher for those surgeons who have attended a full Lund-MAZE training course, and wish to gain an update on the latest thinking with regards to the surgical treatment of Atrial Fibrillation.
We will start with an overview of the disease burden, talk to the foundation clinical evidence available, and cover the various lesion sets used by surgeons – with a view to simplifying the procedure. The workshop will also explain the technology used, how to treat the Left Atrial Appendage, the best ways to work with your EP colleagues, and involve a short hands-on session to familiarize you with the tools available to perform the Lund-MAZE procedure.

Faculty
{{image}}
Mr. Declan Harlow
Cardiothoracic Surgeon

Mr Harlows training was completed at the Brenhill Clinic, Rochester, Minnesota, between June 1995 and July 1997 followed by an advanced fellowship with Professor Ferris K Lomond at the Ashgrove General Hospital. Additional expertise required visits to Belgium, Italy, England and the United States. Mr Harlow now proctors internationally in order to share his knowledge and further improvement in all areas of minimal access and open cardiac and thoracic surgery.
Further overseas experience at the Ashgrove General Hospital in Canada culminated in the award of Clinical Fellowship in Cardiovascular Surgery in December 1997.

Mr Harlow has contributed to many publications and is referee for Journal articles in very highly regarded professional journals. He performs both Cardiac surgery procedures and thoracic procedures at Westmere Private Hospital and Dunmore Hospital, Melbourne. Mr Harlow has performed in excess of 200 open Maze procedures and 35 via a Thoracoscopic approach.

Venue - TBA
Time : 5pm - 7.30pm, followed by dinner and case presentations

```html
<!DOCTYPE html>
<html lang="en">
<head>
<meta charset="utf-8">
<title>Simplifying the MAZE – Field Update</title>
<link href="https://fonts.googleapis.com/css2?family=Arimo:ital,wght@0,400;0,700;1,400&display=swap" rel="stylesheet">
<style>
  :root {
    --bg: #f2b886;
    --paper: #ffffff;
    --sidebar: #ebebeb;
    --orange: #e2761f;
    --blue: #1f6fb2;
    --text: #4a4a4a;
    --muted: #777777;
    --ink: #3a3a3a;
  }
  * { box-sizing: border-box; margin: 0; padding: 0; }
  html, body { width: 1200px; height: 878px; overflow: hidden; }
  body {
    background: var(--bg);
    font-family: "Arimo", Arial, sans-serif;
    color: var(--text);
    position: relative;
  }
  .flyer {
    position: absolute;
    left: 300px; top: 14px;
    width: 600px; height: 850px;
    background: var(--paper);
    box-shadow: 0 10px 30px rgba(120, 60, 10, 0.25);
    overflow: hidden;
  }
  .sidebar {
    position: absolute; left: 0; top: 0;
    width: 96px; height: 100%;
    background: var(--sidebar);
  }
  .date-box {
    position: absolute; left: 20px; top: 118px;
    width: 68px; height: 68px;
    background: var(--orange);
    color: #fff;
    display: flex; flex-direction: column; justify-content: center; align-items: center;
    line-height: 1;
  }
  .date-box .day { font-size: 12px; letter-spacing: 0.5px; }
  .date-box .year { font-size: 21px; margin-top: 3px; }
  .tab {
    position: absolute; left: 96px; top: 96px;
    width: 220px; height: 46px;
  }
  .tab-label {
    position: absolute; left: 118px; top: 110px;
    color: #fff; font-weight: 700; font-size: 14px; letter-spacing: 0.6px;
  }
  .brand {
    position: absolute; right: 48px; top: 64px;
    font-size: 26px; font-weight: 700; color: var(--ink);
    letter-spacing: 0;
  }
  .rule {
    position: absolute; left: 108px; top: 142px;
    width: 2px; height: 650px; background: var(--orange);
  }
  .content {
    position: absolute; left: 128px; top: 160px; width: 430px;
  }
  .title {
    font-size: 31px; font-weight: 700; color: var(--blue); letter-spacing: -0.3px; line-height: 1.1;
  }
  .lead { font-size: 11.5px; line-height: 1.4; margin-top: 10px; color: #444; }
  .intro { font-size: 7.6px; line-height: 1.55; margin-top: 8px; color: var(--orange); }
  .faculty-row { position: relative; margin-top: 14px; height: 150px; }
  .faculty-label { font-size: 10px; font-weight: 700; color: var(--blue); }
  .portrait {
    position: absolute; left: 0; top: 16px;
    width: 108px; height: 112px;
    border: 2px solid var(--orange);
    background: linear-gradient(160deg, #6a5b4d 0%, #3c332c 60%, #1f1b18 100%);
  }
  .trace {
    position: absolute; left: 112px; top: 0; width: 318px; height: 90px;
    background: linear-gradient(90deg, rgba(230,230,230,0) 0%, rgba(215,215,215,0.7) 45%, rgba(230,230,230,0.3) 100%);
  }
  .name { position: absolute; left: 0; top: 132px; font-size: 8.5px; font-weight: 700; color: #222; }
  .role { position: absolute; left: 0; top: 143px; font-size: 8px; font-style: italic; color: var(--muted); }
  .bio { margin-top: 14px; }
  .bio p { font-size: 7.6px; line-height: 1.6; margin-bottom: 8px; color: #555; }
  .details { margin-top: 6px; font-size: 8.5px; font-weight: 700; color: var(--blue); line-height: 1.5; }
</style>
</head>
<body>
  <main class="flyer">
    <div class="sidebar"></div>
    <div class="date-box"><span class="day">16 DEC</span><span class="year">2019</span></div>

    <svg class="tab" viewBox="0 0 220 46" aria-hidden="true">
      <path d="M0 0 H170 Q190 0 200 20 Q210 42 220 46 H0 Z" fill="#e2761f"/>
      <path d="M0 0 H162 Q182 0 192 20 Q201 40 212 46 H0 Z" fill="#1f6fb2"/>
    </svg>
    <div class="tab-label">FIELD UPDATE</div>

    <div class="brand">VerdaCore</div>

    <div class="rule"></div>

    <section class="content">
      <h1 class="title">Simplifying the MAZE</h1>
      <p class="lead">This short workshop is designed as a refresher for those surgeons who have attended a full Lund-MAZE training course, and wish to gain an update on the latest thinking with regards to the surgical treatment of Atrial Fibrillation.</p>
      <p class="intro">We will start with an overview of the disease burden, talk to the foundation clinical evidence available, and cover the various lesion sets used by surgeons – with a view to simplifying the procedure. The workshop will also explain the technology used, how to treat the Left Atrial Appendage, the best ways to work with your EP colleagues, and involve a short hands-on session to familiarize you with the tools available to perform the Lund-MAZE procedure.</p>

      <div class="faculty-row">
        <h2 class="faculty-label">FACULTY</h2>
        <div class="portrait" role="img" aria-label="Portrait photo of Mr. Declan Harlow"></div>
        <div class="trace" role="img" aria-label="Faint heart rhythm trace on a grid"></div>
        <div class="name">Mr. Declan Harlow</div>
        <div class="role">Cardiothoracic Surgeon</div>
      </div>

      <div class="bio">
        <p>Mr Harlows training was completed at the Brenhill Clinic, Rochester, Minnesota, between June 1995 and July 1997 followed by an advanced fellowship with Professor Ferris K Lomond at the Ashgrove General Hospital. Additional expertise required visits to Belgium, Italy, England and the United States. Mr Harlow now proctors internationally in order to share his knowledge and further improvement in all areas of minimal access and open cardiac and thoracic surgery.</p>
        <p>Further overseas experience at the Ashgrove General Hospital in Canada culminated in the award of Clinical Fellowship in Cardiovascular Surgery in December 1997.</p>
        <p>Mr Harlow has contributed to many publications and is referee for Journal articles in very highly regarded professional journals. He performs both Cardiac surgery procedures and thoracic procedures at Westmere Private Hospital and Dunmore Hospital, Melbourne. Mr Harlow has performed in excess of 200 open Maze procedures and 35 via a Thoracoscopic approach.</p>
      </div>

      <div class="details">
        <div>Venue: TBA</div>
        <div>Time: 5pm - 7.30pm, followed by dinner and case presentations</div>
      </div>
    </section>
  </main>
</body>
</html>
```